Letterhead

Can you please design me a letterhead that I can use electronically in word as a template. I have attached my business card as I would like the design to reflect this logo.

```html
<!DOCTYPE html>
<html lang="en">
<head>
<meta charset="utf-8">
<title>Tallowick Letterhead</title>
<link href="https://fonts.googleapis.com/css2?family=Arimo:wght@400;700&family=Open+Sans:wght@400;600&display=swap" rel="stylesheet">
<style>
  :root {
    --backdrop: #ececec;
    --paper: #ffffff;
    --ink-black: #1d1a19;
    --brand-red: #a32626;
    --text-grey: #5a5a5a;
    --tagline-white: #f2f2f2;
  }
  * { margin: 0; padding: 0; box-sizing: border-box; }
  html, body {
    width: 1200px;
    height: 950px;
    overflow: hidden;
    background: var(--backdrop);
  }
  .canvas {
    position: relative;
    width: 1200px;
    height: 950px;
  }
  .letterhead {
    position: absolute;
    left: 289px;
    top: 35px;
    width: 622px;
    height: 880px;
    background: var(--paper);
    box-shadow: 0 2px 10px rgba(0, 0, 0, 0.12);
    overflow: hidden;
  }
  .header-band {
    position: absolute;
    left: 0;
    top: 0;
    width: 100%;
    height: 170px;
    background: var(--ink-black);
  }
  .brand {
    position: absolute;
    left: 190px;
    top: 52px;
    display: flex;
    flex-direction: column;
    align-items: flex-end;
  }
  .brand-name {
    font-family: "Arimo", Arial, sans-serif;
    font-weight: 700;
    font-size: 54px;
    line-height: 1;
    letter-spacing: 1px;
    color: var(--brand-red);
  }
  .brand-tagline {
    margin-top: 4px;
    font-family: "Arimo", Arial, sans-serif;
    font-weight: 400;
    font-size: 11.5px;
    color: var(--tagline-white);
  }
  .contact-line {
    position: absolute;
    right: 22px;
    bottom: 62px;
    font-family: "Open Sans", Arial, sans-serif;
    font-size: 12.5px;
    color: var(--text-grey);
    white-space: nowrap;
  }
  .contact-label { color: var(--brand-red); font-weight: 600; }
  .contact-divider { color: var(--brand-red); margin: 0 4px; }
  .footer-band {
    position: absolute;
    left: 0;
    bottom: 0;
    width: 100%;
    height: 42px;
    background: var(--brand-red);
  }
  .footer-block {
    position: absolute;
    right: 0;
    bottom: 0;
    width: 78px;
    height: 42px;
    background: var(--ink-black);
  }
</style>
</head>
<body>
  <main class="canvas">
    <article class="letterhead">
      <header class="header-band">
        <div class="brand">
          <span class="brand-name">tallowick</span>
          <span class="brand-tagline">Business Consultants Pty Ltd</span>
        </div>
      </header>

      <p class="contact-line">
        <span class="contact-label">P</span> : 0412 555 018
        <span class="contact-divider">|</span>
        <span class="contact-label">E</span> : helen@tallowick.net.au
        <span class="contact-divider">|</span>
        <span class="contact-label">ACN</span> : 041 552 806
      </p>

      <footer class="footer-band"></footer>
      <div class="footer-block"></div>
    </article>
  </main>
</body>
</html>
```